Business Card Design

We are a General Practice - Family medicine
We also have Allied Health professionals working within our team

Industry/Entity Type

Business

Contact Information for Business Card

Front of the card to display:

BRAMBLEWICK MEDICAL
PHONE 6348 2917

5/41 Fennimore Parade
Launceston Tasmania 7284

Back of the card to display:

My Appointments
Date:
Time:
With:

Please remember to phone us on 6348 2917 to cancel your appointment if you can't keep it.
A fee applied to missed appointments

```html
<!DOCTYPE html>
<html lang="en">
<head>
<meta charset="utf-8">
<title>Bramblewick Medical – Appointment Card</title>
<link rel="stylesheet" href="https://fonts.googleapis.com/css2?family=Catamaran:wght@400&family=Open+Sans:wght@400;700&display=swap">
<style>
  :root {
    --brand-blue: #2aa6dc;
    --ribbon-blue: #12a8e1;
    --text-blue: #19a9df;
    --label-grey: #9a9a9a;
    --tagline-grey: #555555;
    --paper: #ffffff;
    --dot-blue: #2ab0e4;
  }
  html, body {
    margin: 0;
    padding: 0;
    overflow: hidden;
    background: var(--paper);
  }
  .card {
    position: relative;
    width: 686px;
    height: 1200px;
    background: var(--paper);
    overflow: hidden;
    font-family: "Open Sans", Arial, sans-serif;
  }
  .brand-dot {
    position: absolute;
    left: 283px;
    top: 130px;
    width: 120px;
    height: 120px;
    border-radius: 50%;
    background: var(--brand-blue);
  }
  .brand-name {
    position: absolute;
    left: 0;
    top: 318px;
    width: 686px;
    margin: 0;
    text-align: center;
    font-family: "Catamaran", Arial, sans-serif;
    font-weight: 400;
    font-size: 60px;
    line-height: 80px;
    color: var(--brand-blue);
  }
  .tagline {
    position: absolute;
    left: 0;
    top: 438px;
    width: 686px;
    margin: 0;
    text-align: center;
    font-size: 22px;
    letter-spacing: 6px;
    color: var(--tagline-grey);
  }
  .ribbon {
    position: absolute;
    left: 103px;
    top: 506px;
    width: 492px;
    height: 98px;
  }
  .ribbon-label {
    position: absolute;
    left: 103px;
    top: 506px;
    width: 492px;
    height: 98px;
    margin: 0;
    display: flex;
    align-items: center;
    justify-content: center;
    font-size: 50px;
    font-weight: 400;
    color: var(--paper);
  }
  .field {
    position: absolute;
    left: 43px;
    width: 540px;
    height: 50px;
    border-bottom: 4px dotted var(--dot-blue);
  }
  .field-label {
    position: absolute;
    left: 0;
    bottom: -2px;
    font-size: 35px;
    color: var(--label-grey);
  }
  .field--date { top: 672px; }
  .field--time { top: 788px; }
  .field--with { top: 904px; }
  .notice {
    position: absolute;
    left: 0;
    top: 968px;
    width: 686px;
    margin: 0;
    text-align: center;
    color: var(--text-blue);
    font-weight: 700;
  }
  .notice-line { display: block; }
  .notice-lead { font-size: 25px; line-height: 36px; }
  .notice-phone { font-size: 37px; line-height: 48px; }
  .notice-cancel { font-size: 24px; line-height: 36px; }
  .notice-fee { font-size: 29px; line-height: 40px; margin-top: 14px; }
</style>
</head>
<body>
<div class="card">
  <div class="brand-dot" aria-hidden="true"></div>
  <h1 class="brand-name">Bramblewick Medical</h1>
  <p class="tagline">HEALTHCARE CENTRE</p>

  <svg class="ribbon" viewBox="0 0 492 98" aria-hidden="true">
    <path d="M0 4 Q246 -6 492 4 L460 49 L492 94 Q246 84 0 94 L32 49 Z" fill="var(--ribbon-blue)"/>
  </svg>
  <p class="ribbon-label">APOINTMENT</p>

  <div class="field field--date"><span class="field-label">Date</span></div>
  <div class="field field--time"><span class="field-label">Time</span></div>
  <div class="field field--with"><span class="field-label">With</span></div>

  <p class="notice">
    <span class="notice-line notice-lead">Please remember to phone us on</span>
    <span class="notice-line notice-phone">6348 2917</span>
    <span class="notice-line notice-cancel">to cancel your appointment if you can't keep it.</span>
    <span class="notice-line notice-fee">A fee applied to missed appointments</span>
  </p>
</div>
</body>
</html>
```